Harbourline Bathrooms Business Card Design

Under Logo i would like our slogan: Quality bathrooms made affordable. Also on the card i would like: Free no obligation quotes. Our company is a bathroom renovation company.

Industry/Entity Type

Business

Contact Information for Business Card

Mark Pellowe, Mark@harbourlinebathrooms.co.nz, 021 473 2951, 0800 47 TUBS www.harbourlinebathrooms.co.nz

Requirements
Must have
• Include my logo. Green colours used

```html
<!DOCTYPE html>
<html lang="en">
<head>
<meta charset="utf-8">
<title>Harbourline Bathrooms – Business Card</title>
<link rel="stylesheet" href="https://fonts.googleapis.com/css2?family=Oswald:wght@400;500&family=Kalam:wght@400&family=Arimo:wght@400&display=swap">
<style>
  :root {
    --page-bg: #d9d5cf;
    --card-bg: #efeeec;
    --panel-dark: #2e2e2e;
    --accent-green: #6ab04c;
    --accent-glint: #fafafa;
    --name-grey: #cfcfcf;
    --contact-light: #e4e4e4;
    --brand-ink: #3a3a3a;
  }
  * { margin: 0; padding: 0; box-sizing: border-box; }
  html, body {
    width: 1200px; height: 970px; overflow: hidden;
    background: var(--page-bg);
  }
  .business-card {
    position: absolute; left: 172px; top: 270px;
    width: 856px; height: 475px;
    background: var(--card-bg);
    box-shadow: 0 6px 24px rgba(0,0,0,0.18);
    overflow: hidden;
  }
  .card-shapes { position: absolute; inset: 0; }
  .owner-name {
    position: absolute; left: 64px; top: 174px;
    font: 500 36px/1 'Oswald', sans-serif;
    color: var(--name-grey); letter-spacing: 0.5px;
  }
  .job-title {
    position: absolute; left: 64px; top: 224px;
    font: 500 20px/1 'Oswald', sans-serif;
    color: var(--accent-green); letter-spacing: 1.5px;
  }
  .contact-line {
    position: absolute; left: 64px;
    display: flex; align-items: center; gap: 12px;
    font: 400 19px/1 'Oswald', sans-serif;
    color: var(--contact-light); letter-spacing: 0.3px;
  }
  .contact-line svg { width: 24px; height: 18px; fill: var(--accent-green); }
  .contact-phone { top: 262px; }
  .contact-email { top: 300px; }
  .offer-note {
    position: absolute; right: 40px; top: 40px;
    font: 500 21px/1 'Oswald', sans-serif;
    color: var(--accent-green); letter-spacing: 1px;
  }
  .brand-name {
    position: absolute; left: 478px; top: 327px;
    font: 400 26px/1 'Arimo', sans-serif;
    color: var(--brand-ink);
  }
  .brand-tagline {
    position: absolute; left: 492px; top: 368px;
    font: 400 18px/1 'Kalam', cursive;
    color: var(--brand-ink);
    transform: rotate(-3deg); transform-origin: left center;
  }
  .brand-website {
    position: absolute; left: 494px; top: 412px;
    font: 400 22px/1 'Oswald', sans-serif;
    color: var(--accent-green); letter-spacing: 0.5px;
  }
</style>
</head>
<body>
  <div class="business-card">
    <svg class="card-shapes" viewBox="0 0 856 475" width="856" height="475" aria-hidden="true">
      <path class="dark-panel" d="M0,0 L318,0 Q560,192 283,475 L0,475 Z" fill="var(--panel-dark)"/>
      <path class="panel-glint" d="M333,0 Q578,192 295,475" fill="none" stroke="var(--accent-glint)" stroke-width="8"/>
      <path class="green-arc" d="M348,0 Q596,192 308,475" fill="none" stroke="var(--accent-green)" stroke-width="12"/>
    </svg>

    <div class="owner-name">Mark Pellowe</div>
    <div class="job-title">JOB TITTLE</div>

    <div class="contact-line contact-phone">
      <svg viewBox="0 0 26 20"><path d="M2,7 C2,2 24,2 24,7 L24,9 L18,9 L18,6.5 C15,5.5 11,5.5 8,6.5 L8,9 L2,9 Z M6,10 L20,10 L23,18 L3,18 Z"/></svg>
      <span>021 473 2951 &nbsp;|&nbsp; 0800 47 TUBS</span>
    </div>
    <div class="contact-line contact-email">
      <svg viewBox="0 0 26 20"><path d="M2,4 L24,4 L24,17 L2,17 Z"/><path d="M2,4 L13,12 L24,4" fill="none" stroke="var(--panel-dark)" stroke-width="1.6"/></svg>
      <span>Mark@harbourlinebathrooms.co.nz</span>
    </div>

    <div class="offer-note">FREE NO OBLIGATION QUOTES</div>

    <div class="brand-name">Harbourline Bathrooms Ltd</div>
    <div class="brand-tagline">Quality bathrooms made affordable</div>
    <div class="brand-website">www.harbourlinebathrooms.co.nz</div>
  </div>
</body>
</html>
```